Business card design for sustainable building and development company

Need a business card design for a new sustainable building and real estate development company in the San Francisco Bay area. Name of company is "Norvale Advisors, LLC" and we provide "Sustainable building, energy and development services" for residential and non residential projects. We'd like the following colors used but not all area required: green, gray, blue. Design should communicate innovation, professionalism and sustainability. Our current website is www.norvale-advisors.example. Another possible design idea is to have the following listed on the back of the card:
Certified: TRAM QX, Leaf Mark Grader, VOLT Grader, EcoState Examiner, RDQ HX Building Analyst. Its not a must but could be text that could be used for back of card. Overall, we are open to a simple, clean design and or one with more text than usual for a card.

Industry/Entity Type

Real Estate

Contact Information for Business Card

Name on card: Dmitri L. Hasby
Title for Name: Principal + Founder
Phone: 555.418.2096
Email: dhasby@norvale-advisors.example
Website: www.norvale-advisors.example

Also, please add the following for address:
San Francisco, California

Requirements
Nice to have
• If you can integrate the outline of a skyline on the backside of the card and if it looks good, I would like to see the design
Should not have
• a barcode;

```html
<!DOCTYPE html>
<html lang="en">
<head>
<meta charset="utf-8">
<title>Norvale Advisors – Business Card</title>
<link rel="stylesheet" href="https://fonts.googleapis.com/css2?family=Montserrat:wght@500;700&family=Open+Sans:wght@400&family=PT+Sans:wght@400&display=swap">
<style>
  :root {
    --green: #6abf45;
    --ink: #111111;
    --ink-soft: #3a3a3a;
    --band-gray: #e1e2e4;
    --ghost: #f1f1f1;
    --paper: #ffffff;
    --backdrop: #cfcfcf;
  }
  * { margin: 0; padding: 0; box-sizing: border-box; }
  html, body { width: 1200px; height: 1000px; overflow: hidden; }
  body { background: var(--backdrop); position: relative; }

  .card { position: absolute; background: var(--paper); overflow: hidden; }

  /* Front */
  .card-front { left: 42px; top: 27px; width: 780px; height: 453px; }
  .certifications {
    position: absolute; left: 16px; top: 12px;
    font-family: "Open Sans", sans-serif; font-size: 15.5px; color: var(--green);
    white-space: nowrap;
  }
  .brand-mark {
    position: absolute; left: 73px; top: 155px; width: 160px; height: 160px;
    border-radius: 50%; background: var(--green);
  }
  .brand-name {
    position: absolute; left: 243px; top: 186px;
    font-family: "Montserrat", sans-serif; font-weight: 700; font-size: 48px;
    color: var(--green); white-space: nowrap; letter-spacing: -0.5px;
  }
  .brand-tagline {
    position: absolute; left: 245px; top: 247px;
    font-family: "Montserrat", sans-serif; font-weight: 500; font-size: 14.5px;
    color: var(--ink); white-space: nowrap;
  }
  .front-band {
    position: absolute; left: 0; bottom: 0; width: 100%; height: 33px;
    background: var(--green);
  }
  .location-tab {
    position: absolute; left: 325px; top: 397px; width: 405px; height: 56px;
    background: var(--green); border-radius: 16px 16px 0 0;
    font-family: "Open Sans", sans-serif; font-size: 26px; color: var(--paper);
    letter-spacing: 1px; text-align: center; line-height: 54px;
  }

  /* Back */
  .card-back { left: 373px; top: 517px; width: 785px; height: 446px; }
  .ghost-ring { position: absolute; left: 0; top: 0; }
  .back-band {
    position: absolute; left: 0; bottom: 0; width: 100%; height: 95px;
    background: var(--band-gray);
  }
  .contact-tab {
    position: absolute; left: 312px; top: 328px; width: 423px; height: 40px;
    background: var(--band-gray); border-radius: 18px 18px 0 0;
  }
  .person-name {
    position: absolute; left: 322px; top: 258px;
    font-family: "PT Sans", sans-serif; font-size: 56px; color: var(--ink);
    white-space: nowrap; letter-spacing: -0.5px;
  }
  .contact-list {
    position: absolute; left: 323px; top: 343px; list-style: none;
    font-family: "PT Sans", sans-serif; font-size: 22px; color: var(--ink-soft);
    line-height: 30.5px;
  }
  .contact-label { display: inline-block; width: 46px; }
</style>
</head>
<body>

  <section class="card card-front">
    <p class="certifications">Certified: TRAM QX, Leaf Mark Grader, VOLT Grader, EcoState Examiner, RDQ HX Building Analyst</p>
    <div class="brand-mark"></div>
    <h1 class="brand-name">Norvale Advisors</h1>
    <p class="brand-tagline">SUSTAINABLE BUILDING, ENERGY &amp; DEVELOPMENT SERVICES</p>
    <div class="front-band"></div>
    <div class="location-tab">San Francisco, California</div>
  </section>

  <section class="card card-back">
    <svg class="ghost-ring" width="785" height="446" viewBox="0 0 785 446" aria-hidden="true">
      <circle cx="260" cy="180" r="235" fill="none" stroke="var(--ghost)" stroke-width="40"/>
    </svg>
    <div class="back-band"></div>
    <div class="contact-tab"></div>
    <h2 class="person-name">Dmitri L. Hasby</h2>
    <ul class="contact-list">
      <li><span class="contact-label">[t]</span>555.418.2096</li>
      <li><span class="contact-label">[e]</span>dhasby@norvale-advisors.example</li>
      <li><span class="contact-label">[w]</span>www.norvale-advisors.example</li>
    </ul>
  </section>

</body>
</html>
```